Business Card - Rebranding for Consulting Firm

We are renaming and rebranding our consulting firm and need to raise the level of quality of our cards as part of that effort. We consult to leading high tech, life science and other innovation sector companies.

Need a two-sided business card design.

Side 1: (a) Company logo (b) tag line: Aligning Your People with Your Purpose (c) Name (d) Title (e) Phone 1: Office (f) Phone 2: Mobile (g) email: person@QuillharborAdvisory.com

Side 2: Two lines of text: (a) Markets Shift. Teams Adapt. People Deliver Results. (b) We help you lead through all three.

Target Market(s)

Business and human resources executives and senior managers

Industry/Entity Type

Management Consulting

Contact Information for Business Card

Font styles to use
Sans Serif

Requirements
Must have
• clean, not too busy, but with a bit of creativity. Stick to the colors used in the attached logo
• appeal to high tech, life science companies
Nice to have
• prefer white background

```html
<!DOCTYPE html>
<html lang="en">
<head>
<meta charset="utf-8">
<title>Quillharbor Advisory – Business Card</title>
<link href="https://fonts.googleapis.com/css2?family=Lato:ital,wght@0,400;0,700;1,400&display=swap" rel="stylesheet">
<style>
  :root {
    --brand-blue: #1187c0;
    --brand-deep: #0a6fa3;
    --brand-light: #2ba3d6;
    --stripe-grey: #8fa3b0;
    --text-grey: #5d6670;
    --card-white: #f9fafb;
    --page-bg: #e7e9ec;
  }
  * { margin: 0; padding: 0; box-sizing: border-box; }
  html, body { width: 1200px; height: 780px; overflow: hidden; }
  body {
    background: var(--page-bg);
    font-family: "Lato", Arial, sans-serif;
    position: relative;
  }
  .card {
    position: absolute;
    width: 540px;
    height: 310px;
    background: var(--card-white);
    box-shadow: 0 6px 18px rgba(0,0,0,0.15);
    overflow: hidden;
  }
  .card-front { left: 60px; top: 70px; }
  .card-back { left: 600px; top: 400px; }
  .card svg.swoosh { position: absolute; inset: 0; }

  .brand {
    position: absolute;
    left: 36px;
    top: 112px;
    display: flex;
    align-items: center;
    gap: 10px;
  }
  .brand-square {
    width: 24px; height: 24px;
    background: var(--brand-blue);
  }
  .brand-name {
    color: var(--brand-blue);
    font-size: 25px;
    font-weight: 400;
    letter-spacing: 0.3px;
    white-space: nowrap;
  }
  .tagline {
    position: absolute;
    left: 38px;
    top: 152px;
    color: var(--brand-light);
    font-size: 12px;
    letter-spacing: 1.2px;
    white-space: nowrap;
  }
  .person {
    position: absolute;
    left: 38px;
    top: 210px;
  }
  .person-name {
    color: var(--brand-deep);
    font-size: 16px;
    font-weight: 700;
    letter-spacing: 0.5px;
    text-transform: uppercase;
  }
  .person-title {
    color: var(--text-grey);
    font-size: 12px;
    margin-top: 2px;
  }
  .accent-block {
    position: absolute;
    left: 36px;
    bottom: 0;
    width: 48px;
    height: 12px;
    background: var(--brand-light);
  }
  .contacts {
    position: absolute;
    left: 300px;
    top: 22px;
    list-style: none;
    color: var(--text-grey);
    font-size: 11px;
  }
  .contacts li { display: flex; align-items: center; gap: 7px; margin-bottom: 5px; white-space: nowrap; }
  .contacts svg { width: 13px; height: 13px; flex: none; }

  .message {
    position: absolute;
    left: 160px;
    right: 24px;
    top: 124px;
    color: var(--brand-blue);
    font-size: 13px;
    font-style: italic;
    text-align: center;
    line-height: 2;
  }
  .message p { white-space: nowrap; }
</style>
</head>
<body>

<section class="card card-front" aria-label="Card front">
  <svg class="swoosh" width="540" height="310" viewBox="0 0 540 310" aria-hidden="true">
    <path d="M540 96 C 470 130, 420 200, 300 310 L 318 310 C 430 210, 480 150, 540 118 Z" fill="var(--stripe-grey)" opacity="0.7"/>
    <path d="M540 124 C 480 158, 440 220, 340 310 L 540 310 Z" fill="var(--brand-blue)"/>
    <path d="M540 124 C 480 158, 440 220, 340 310 L 380 310 C 460 230, 500 180, 540 160 Z" fill="var(--brand-light)" opacity="0.5"/>
  </svg>

  <ul class="contacts">
    <li>
      <svg viewBox="0 0 14 14"><rect width="14" height="14" rx="2" fill="var(--brand-blue)"/><path d="M4 3.5 h2 l.7 2 -1 .8 a5 5 0 0 0 2 2 l.8-1 2 .7 v2 a1 1 0 0 1-1 1 A7 7 0 0 1 3 4.5 a1 1 0 0 1 1-1z" fill="#fff"/></svg>
      (01) 5550 0142
    </li>
    <li>
      <svg viewBox="0 0 14 14"><rect width="14" height="14" rx="2" fill="var(--brand-blue)"/><rect x="4.5" y="2.5" width="5" height="9" rx="1" fill="#fff"/><rect x="5.5" y="3.8" width="3" height="5" fill="var(--brand-blue)"/></svg>
      (01) 5550 0178
    </li>
    <li>
      <svg viewBox="0 0 14 14"><rect width="14" height="14" rx="2" fill="var(--brand-blue)"/><rect x="2.5" y="4" width="9" height="6" fill="#fff"/><path d="M2.5 4 L7 7.5 L11.5 4" stroke="var(--brand-blue)" fill="none"/></svg>
      person@QuillharborAdvisory.com
    </li>
  </ul>

  <div class="brand">
    <span class="brand-square"></span>
    <span class="brand-name">Quillharbor Advisory LLC</span>
  </div>
  <p class="tagline">Aligning Your People with Your Purpose</p>

  <div class="person">
    <p class="person-name">Dana Whitlow</p>
    <p class="person-title">Director</p>
  </div>
  <span class="accent-block"></span>
</section>

<section class="card card-back" aria-label="Card back">
  <svg class="swoosh" width="540" height="310" viewBox="0 0 540 310" aria-hidden="true">
    <path d="M0 0 L40 0 C 40 120, 90 230, 140 310 L0 310 Z" fill="var(--brand-blue)"/>
    <path d="M0 0 L40 0 C 40 120, 90 230, 140 310 L110 310 C 70 240, 30 140, 22 0 Z" fill="var(--brand-deep)" opacity="0.5"/>
    <path d="M52 0 C 54 120, 104 228, 156 310" stroke="var(--stripe-grey)" stroke-width="4" fill="none" opacity="0.8"/>
  </svg>
  <div class="message">
    <p>Markets Shift. Teams Adapt. People Deliver Results.</p>
    <p>We help you lead through all three.</p>
  </div>
</section>

</body>
</html>
```